Business Card design for a company called Tallow Flame NI

I need a business card design for my oil fired boiler servicing company. I have a logo design already and Im just looking that incorporated into the business card design. card details; Tallow Flame NI
Oil Burner Servicing - Mid Ulster Area
Service Engineer - Owen Marsh
Mobile 07751364927
email - Tallow.Flame.NI@hearthmail.example
www.tallowflameni.example
I carry out Servicing, Commissioning, Fault Finding, Warranty Validation
Target Market(s)
home owners with oil fired central heating
Industry/Entity Type
Business
Contact Information for Business Card
Tallow Flame NI
Tell. 07751364927
Web: www.tallowflameni.example
email Tallow.Flame.NI@Hearthmail.Example
Servicing Fault Finding Commissioning Warranty Validation
Look and feel

```html
<!DOCTYPE html>
<html lang="en">
<head>
<meta charset="utf-8">
<title>Tallow Flame NI – Business Cards</title>
<link rel="stylesheet" href="https://fonts.googleapis.com/css2?family=Arimo:wght@400;700&family=Roboto+Condensed:wght@400&display=swap">
<style>
  :root {
    --page-bg: #ececec;
    --card-black: #050505;
    --brand-green: #5cbf3a;
    --card-white: #ffffff;
    --ink: #111111;
  }
  * { box-sizing: border-box; margin: 0; padding: 0; }
  html, body { width: 1200px; height: 1200px; overflow: hidden; }
  body { background: var(--page-bg); position: relative; }

  .card-slot {
    position: absolute;
    left: 205px;
    width: 822px;
    height: 456px;
    overflow: hidden;
    box-shadow: 0 6px 18px rgba(0,0,0,.25);
  }
  .card-slot--green { top: 114px; }
  .card-slot--white { top: 629px; }

  .card {
    position: absolute; left: 0; top: 0;
    width: 1027px; height: 570px;
    transform: scale(0.8);
    transform-origin: 0 0;
  }
  .card__shapes { position: absolute; inset: 0; width: 100%; height: 100%; }

  .brand { position: absolute; left: 92px; top: 70px; height: 96px; display: flex; align-items: center; gap: 18px; }
  .brand__dot { width: 96px; height: 96px; border-radius: 50%; background: var(--brand-green); flex: none; }
  .brand__name {
    font-family: "Arimo", sans-serif; font-weight: 700; font-size: 48px;
    color: var(--brand-green); line-height: 1; letter-spacing: -0.5px;
  }

  .contacts { position: absolute; left: 100px; top: 292px; list-style: none; }
  .contacts__item {
    display: flex; align-items: center; height: 45.5px;
    font-family: "Roboto Condensed", sans-serif; font-size: 27px; color: var(--ink);
    white-space: nowrap;
  }
  .contacts__icon { width: 28px; height: 28px; margin-right: 24px; flex: none; }
  .contacts__at { font-family: "Arimo", sans-serif; font-weight: 700; font-size: 24px; width: 28px; margin-right: 24px; text-align: center; }

  .person { position: absolute; left: 622px; top: 358px; color: var(--ink); }
  .person__name { font-family: "Arimo", sans-serif; font-size: 58px; line-height: 1; letter-spacing: -0.5px; white-space: nowrap; }
  .person__role { font-family: "Arimo", sans-serif; font-size: 29px; margin-top: 8px; }
</style>
</head>
<body>

<svg width="0" height="0" style="position:absolute" aria-hidden="true">
  <defs>
    <linearGradient id="band-gradient" x1="0" y1="0" x2="0.35" y2="1">
      <stop offset="0" stop-color="#d6e22a"/>
      <stop offset="0.45" stop-color="#b2d43a"/>
      <stop offset="1" stop-color="#8cc641"/>
    </linearGradient>
    <symbol id="icon-pin" viewBox="0 0 24 24"><path d="M12 2a7 7 0 0 0-7 7c0 5 7 13 7 13s7-8 7-13a7 7 0 0 0-7-7zm0 10a3 3 0 1 1 0-6 3 3 0 0 1 0 6z" fill="#111"/></symbol>
    <symbol id="icon-phone" viewBox="0 0 24 24"><path d="M8 2.5 10 7 8.3 8.6c.6 2.8 2.3 5.6 4.4 7.4L14.4 14.5 18.5 17l-1 3.8C10 21 4.5 13 6 3.2z" fill="#111"/></symbol>
    <symbol id="icon-globe" viewBox="0 0 24 24"><g fill="none" stroke="#111" stroke-width="1.8"><circle cx="12" cy="12" r="9"/><ellipse cx="12" cy="12" rx="4" ry="9"/><path d="M3 12h18M4.5 7.5h15M4.5 16.5h15"/></g></symbol>
  </defs>
</svg>

<!-- Green front -->
<div class="card-slot card-slot--green">
  <article class="card">
    <svg class="card__shapes" viewBox="0 0 1027 570" aria-hidden="true">
      <rect width="1027" height="570" fill="url(#band-gradient)"/>
      <polygon points="0,0 1027,0 1027,248 495,248 485,238 0,238" fill="#050505"/>
      <polygon points="502,255 1027,255 1027,276 523,276" fill="#050505"/>
      <polygon points="0,512 503,512 560,570 0,570" fill="#050505"/>
      <polygon points="534,545 1027,545 1027,552 541,552" fill="#050505"/>
    </svg>
    <div class="brand">
      <span class="brand__dot"></span>
      <span class="brand__name">Tallow Flame NI</span>
    </div>
    <ul class="contacts">
      <li class="contacts__item"><svg class="contacts__icon"><use href="#icon-pin"/></svg>#00 Adress 01, Adress, City</li>
      <li class="contacts__item"><svg class="contacts__icon"><use href="#icon-phone"/></svg>077 51 364 927</li>
      <li class="contacts__item"><span class="contacts__at">@</span>tallow.flame.ni@hearthmail.example</li>
      <li class="contacts__item"><svg class="contacts__icon"><use href="#icon-globe"/></svg>www.tallowflameni.example</li>
    </ul>
    <div class="person">
      <p class="person__name">Owen Marsh</p>
      <p class="person__role">Service Engineer</p>
    </div>
  </article>
</div>

<!-- White front -->
<div class="card-slot card-slot--white">
  <article class="card">
    <svg class="card__shapes" viewBox="0 0 1027 570" aria-hidden="true">
      <rect width="1027" height="570" fill="#ffffff"/>
      <polygon points="0,0 1027,0 1027,248 495,248 485,238 0,238" fill="#050505"/>
      <polygon points="502,255 1027,255 1027,276 523,276" fill="#050505"/>
      <polygon points="0,512 503,512 560,570 0,570" fill="#050505"/>
      <polygon points="534,545 1027,545 1027,552 541,552" fill="#050505"/>
    </svg>
    <div class="brand">
      <span class="brand__dot"></span>
      <span class="brand__name">Tallow Flame NI</span>
    </div>
    <ul class="contacts">
      <li class="contacts__item"><svg class="contacts__icon"><use href="#icon-pin"/></svg>#00 Adress 01, Adress, City</li>
      <li class="contacts__item"><svg class="contacts__icon"><use href="#icon-phone"/></svg>077 51 364 927</li>
      <li class="contacts__item"><span class="contacts__at">@</span>tallow.flame.ni@hearthmail.example</li>
      <li class="contacts__item"><svg class="contacts__icon"><use href="#icon-globe"/></svg>www.tallowflameni.example</li>
    </ul>
    <div class="person">
      <p class="person__name">Owen Marsh</p>
      <p class="person__role">Service Engineer</p>
    </div>
  </article>
</div>

</body>
</html>
```